Eye-catching Yellow Page Ad for Attorney's Office

We need a phone book advertisement for our law office. We practice workers' compensation law, and our clientele consists exclusively of individuals who have been injured on the job. The dimensions of the print ad will be 6" W X 4.54" H.

We've had our current ad for several years, and wanted to get a new one that has been designed by a professional. Being that it's an ad for a law firm, it needs to be professional looking, but we're hoping to have something that looks a little more modern and has eye-catching appeal. We like the text that is included in the ad, and we want to make sure our phone number is very visible. No real preference for color scheme.

I've attached a copy of our current ad. All the information included in there is accurate. Our office name is Thornbury & Lisle, PLLC. The ethical rules for attorney advertising require the PLLC to be included in the ad, but it can be smaller than the other text (see our current ad).

Target Market(s)

Our potential clients are injured workers looking for legal representation in their workers' compensation claim.

Industry/Entity Type

Attorney

Font styles to use
Serif
Sans Serif

Requirements
Must have
• Professional, but stands out from the crowd
Nice to have
• Clean modern design
Should not have
• We don't want it to be too crowded or over-worked.

```html
<!DOCTYPE html>
<html lang="en">
<head>
<meta charset="utf-8">
<title>Thornbury &amp; Lisle, PLLC — Workers' Compensation</title>
<link href="https://fonts.googleapis.com/css2?family=Arimo:wght@400;700&family=Roboto+Condensed:wght@700&display=swap" rel="stylesheet">
<style>
  :root{
    --navy:#213a72;
    --navy-dark:#1c3266;
    --orange:#ef9a1f;
    --gold:#f7c33c;
    --white:#ffffff;
    --ink:#111111;
    --accent-blue:#2b9be0;
  }
  *{margin:0;padding:0;box-sizing:border-box}
  html,body{width:1200px;height:908px;overflow:hidden;background:var(--white)}
  .ad{position:relative;width:1200px;height:908px;background:var(--white);font-family:"Arimo",Arial,sans-serif;overflow:hidden}

  .warm-field{position:absolute;left:0;top:145px;width:1200px;height:625px;
    background:linear-gradient(180deg,var(--orange) 0%,#f3ad2e 40%,var(--gold) 100%)}

  .firm-name{position:absolute;left:36px;top:30px;color:var(--navy);
    font-family:"Roboto Condensed",Arial,sans-serif;font-weight:700;font-size:54px;letter-spacing:.5px;line-height:1}
  .firm-suffix{position:absolute;left:520px;top:34px;color:var(--navy);
    font-family:"Roboto Condensed",Arial,sans-serif;font-weight:700;font-size:13px}
  .logo-rule{position:absolute;left:0;top:128px;width:572px;height:17px;background:var(--navy)}

  .title-box{position:absolute;left:572px;top:0;width:628px;height:220px;background:var(--white);border-bottom-left-radius:26px}
  .title{position:absolute;left:584px;top:0;width:616px;height:208px;background:var(--navy);border-bottom-left-radius:20px;
    color:var(--white);font-weight:700;font-size:60px;line-height:74px;text-align:center;padding-top:30px}

  .tagline{position:absolute;left:53px;top:158px;color:var(--white);
    font-family:"Roboto Condensed",Arial,sans-serif;font-weight:700;font-size:34px;line-height:46px}
  .intro{position:absolute;left:55px;top:255px;width:1120px;color:var(--ink);font-size:22px;line-height:28px}

  .photo-frame{position:absolute;left:40px;top:344px;width:470px;height:440px;background:var(--white);border-top-right-radius:20px}
  .photo{position:absolute;left:53px;top:356px;width:442px;height:410px;border-top-right-radius:14px;
    background:linear-gradient(135deg,#8a5a34 0%,#b58a5c 45%,#5b3a24 100%)}
  .names-strip{position:absolute;left:0;top:766px;width:572px;height:54px;background:var(--white)}
  .attorney-name{position:absolute;top:778px;color:var(--navy);font-size:28px}
  .attorney-name.first{left:87px}
  .attorney-name.second{left:313px}

  .services-head{position:absolute;left:570px;top:297px;width:630px;height:63px;background:var(--navy);border-top-left-radius:18px;
    color:var(--white);font-family:"Roboto Condensed",Arial,sans-serif;font-weight:700;font-size:36px;line-height:63px;text-align:center}
  .services{position:absolute;left:570px;top:360px;width:630px;height:298px;background:var(--white);list-style:none;padding:8px 0 0 98px}
  .services li{position:relative;font-size:30px;line-height:40px;color:var(--ink)}
  .services li::before{content:"";position:absolute;left:-48px;top:13px;width:18px;height:18px;border-radius:50%;background:var(--navy)}
  .services-rule{position:absolute;left:570px;top:656px;width:630px;height:6px;background:linear-gradient(90deg,var(--gold),var(--orange))}

  .values{position:absolute;left:570px;top:662px;width:630px;height:50px;background:var(--white);
    color:var(--navy);font-size:26px;line-height:52px;text-align:center}
  .values .sep{color:var(--accent-blue)}

  .phone{position:absolute;left:584px;top:712px;width:616px;height:110px;background:var(--navy);border-top-left-radius:18px;
    color:var(--white);font-weight:700;padding:6px 0 0 18px;white-space:nowrap}
  .phone .area{font-size:46px}
  .phone .number{font-size:92px;letter-spacing:1px}

  .footer{position:absolute;left:0;top:820px;width:1200px;height:88px;background:var(--navy);color:var(--white)}
  .address{position:absolute;left:36px;top:26px;font-family:"Roboto Condensed",Arial,sans-serif;font-weight:700;font-size:30px}
  .divider{position:absolute;left:629px;top:16px;width:2px;height:52px;background:var(--white)}
  .website{position:absolute;left:666px;top:22px;font-weight:700;font-size:36px}
</style>
</head>
<body>
<div class="ad">
  <div class="warm-field"></div>

  <div class="firm-name">Thornbury &amp; Lisle</div>
  <div class="firm-suffix">PLLC</div>
  <div class="logo-rule"></div>

  <div class="title-box"></div>
  <h1 class="title">WORKERS’<br>COMPENSATION</h1>

  <h2 class="tagline">Former Assistant Attorneys<br>General Who Know The System</h2>
  <p class="intro">At Thornbury &amp; Lisle, we provide personal attention to our clients, that means your case is handled by an attorney, not an assitant.</p>

  <div class="photo-frame"></div>
  <div class="photo" role="img" aria-label="Photo of the two attorneys standing in a law library, one holding an open book"></div>
  <div class="names-strip"></div>
  <span class="attorney-name first">Graham Thornbury</span>
  <span class="attorney-name second" style="left:330px">Elena Lisle</span>

  <h3 class="services-head">We can help with:</h3>
  <ul class="services">
    <li>Workplace Injuries or Death</li>
    <li>Lost Wages</li>
    <li>Medical Expensese &amp; Treatment</li>
    <li>Hearing Loss Claims</li>
    <li>Pension Claims</li>
    <li>Disability Awards</li>
    <li>Return To Work Issues</li>
  </ul>
  <div class="services-rule"></div>

  <p class="values">PROFESSIONAL <span class="sep">|</span> COMMITTER <span class="sep">|</span> EFFECTIVE</p>

  <div class="phone"><span class="area">0360</span><span class="number">555-0142</span></div>

  <footer class="footer">
    <span class="address">42 W. Harbor Street Suite 510, Fairhaven</span>
    <span class="divider"></span>
    <span class="website">www.thornburylisle.com</span>
  </footer>
</div>
</body>
</html>
```